Brevanta Website

I would like to have a revised web site for Brevanta. Brevanta is two companies - Brevanta Insurance Company and Brevanta Re Intermediaries. The logos are set, the site content is set, but the flow and look of the web site is clunky.

We do need a landing page that allows someone to choose either company. The one we have is very basic.

Current photos are not required, just ones we used.

www.brevanta-example.com is the site.

Target Market(s)

Business professionals (insurance)

Industry/Entity Type

Insurance

Requirements
Must have
• Brevanta Insurance Company
• Brevanta Re Intermediaries
• Current logos

```html
<!DOCTYPE html>
<html lang="en">
<head>
<meta charset="utf-8">
<title>Brevanta Re Intermediaries</title>
<link href="https://fonts.googleapis.com/css2?family=Source+Sans+3:wght@400;600;700&display=swap" rel="stylesheet">
<style>
  :root {
    --brand-red: #e3242b;
    --text-grey: #555555;
    --nav-grey: #4a4a4a;
    --dark-panel: #1f1f1f;
    --welcome-pink: #f6a5b0;
    --footer-bg: #ececec;
    --footer-line: #d6d6d6;
    --social-blue: #3b5998;
    --social-sky: #29a9e1;
    --white: #ffffff;
  }
  * { box-sizing: border-box; margin: 0; padding: 0; }
  html, body { width: 1200px; height: 910px; overflow: hidden; }
  body {
    position: relative;
    background: var(--white);
    font-family: "Source Sans 3", "Myriad Pro", Arial, sans-serif;
    color: var(--text-grey);
  }
  .top-rule { position: absolute; left: 0; top: 0; width: 1200px; height: 5px; background: var(--brand-red); }

  .site-header { position: absolute; left: 0; top: 5px; width: 1200px; height: 135px; }
  .brand { position: absolute; left: 100px; top: 62px; display: flex; align-items: center; gap: 10px; }
  .brand-mark { width: 18px; height: 18px; background: var(--brand-red); }
  .brand-name { font-size: 28px; font-weight: 400; color: #2b2f3a; letter-spacing: 0.5px; }

  .call-us { position: absolute; left: 738px; top: 27px; font-size: 17px; color: #9a9a9a; }
  .call-us strong { color: #2b2b2b; font-weight: 600; }
  .search {
    position: absolute; left: 928px; top: 21px; width: 169px; height: 29px;
    border: 1px solid #c9c9c9; background: #f6f6f6;
    font-size: 12px; color: #333; padding: 7px 12px;
  }
  .search svg { position: absolute; right: 9px; top: 6px; }

  .main-nav { position: absolute; top: 91px; left: 737px; display: flex; gap: 0; }
  .main-nav a { font-size: 14.5px; color: var(--nav-grey); text-decoration: none; text-transform: uppercase; margin-right: 41px; }
  .main-nav a.current { color: var(--brand-red); }
  .main-nav a:last-child { margin-right: 0; }

  .hero {
    position: absolute; left: 0; top: 140px; width: 1200px; height: 453px;
    background:
      linear-gradient(180deg, rgba(0,0,0,0) 55%, rgba(30,10,20,0.55) 100%),
      linear-gradient(180deg, #7a3f86 0%, #b5567d 35%, #c96a68 55%, #7a3a40 75%, #3a1c22 100%);
  }
  .hero-arrow {
    position: absolute; top: 204px; width: 42px; height: 42px; border-radius: 50%;
    background: rgba(255,255,255,0.92); display: flex; align-items: center; justify-content: center;
  }
  .hero-arrow.prev { left: 100px; }
  .hero-arrow.next { left: 1058px; }

  .welcome {
    position: absolute; left: 99px; top: 545px; width: 1002px; height: 159px;
    background: var(--dark-panel); text-align: center; padding-top: 18px;
  }
  .welcome h1 { font-size: 25px; font-weight: 400; color: var(--welcome-pink); margin-bottom: 8px; }
  .welcome p { font-size: 17.5px; line-height: 29px; color: var(--white); padding: 0 36px; }
  .welcome a { color: var(--welcome-pink); text-decoration: none; font-size: 15.5px; margin-left: 4px; }

  .services { position: absolute; top: 728px; left: 0; width: 1200px; height: 60px; }
  .service { position: absolute; display: flex; align-items: center; gap: 14px; }
  .service span { color: var(--brand-red); font-size: 20.5px; font-weight: 600; line-height: 25px; }

  .site-footer {
    position: absolute; left: 0; top: 811px; width: 1200px; height: 99px;
    background: var(--footer-bg); border-top: 1px solid var(--footer-line);
  }
  .footer-nav { position: absolute; left: 100px; top: 23px; font-size: 14.5px; color: #555; }
  .footer-nav a { color: #555; text-decoration: none; }
  .footer-nav .sep { margin: 0 9px; }
  .copyright { position: absolute; left: 100px; top: 58px; font-size: 14.5px; color: #555; }
  .social { position: absolute; top: 33px; width: 32px; height: 32px; border-radius: 50%; }
  .social.one { left: 1023px; background: var(--social-blue); }
  .social.two { left: 1067px; background: var(--social-sky); }
</style>
</head>
<body>
  <div class="top-rule"></div>

  <header class="site-header">
    <div class="brand">
      <span class="brand-mark"></span>
      <span class="brand-name">BREVANTA RE</span>
    </div>
    <div class="call-us">CALL US : <strong>555-204-7718</strong></div>
    <div class="search">Search
      <svg width="16" height="16" viewBox="0 0 16 16"><circle cx="6" cy="6" r="4.5" fill="none" stroke="#222" stroke-width="2.2"/><line x1="9.5" y1="9.5" x2="14.5" y2="14.5" stroke="#222" stroke-width="3" stroke-linecap="round"/></svg>
    </div>
    <nav class="main-nav">
      <a class="current" href="#">Home</a>
      <a href="#">About Us</a>
      <a href="#">Services</a>
      <a href="#">Contact Us</a>
    </nav>
  </header>

  <section class="hero" role="img" aria-label="Night city skyline with illuminated towers beneath a pink evening sky">
    <div class="hero-arrow prev"><svg width="14" height="18" viewBox="0 0 14 18"><polyline points="10,2 3,9 10,16" fill="none" stroke="#888" stroke-width="1.6"/></svg></div>
    <div class="hero-arrow next"><svg width="14" height="18" viewBox="0 0 14 18"><polyline points="4,2 11,9 4,16" fill="none" stroke="#888" stroke-width="1.6"/></svg></div>
  </section>

  <section class="welcome">
    <h1>Welcome to BREVANTA RE</h1>
    <p>We are a boutique reinsurance brokerage and advisory firm specialized in providing risk management, strategic consulting and risk transfer services to insurance companies, MGAs and producers alike. Established in 2013, Brevanta Re is a member of the industry leading Halvorsen Group of companies domiciled in Fort Worth, Texas. <a href="#">Know more</a></p>
  </section>

  <section class="services">
    <div class="service" style="left:122px; top:4px;">
      <svg width="58" height="50" viewBox="0 0 58 50" fill="#e3242b">
        <circle cx="17" cy="11" r="9"/><path d="M2 44 Q2 22 17 22 Q30 22 31 34 L31 44 Z"/>
        <circle cx="36" cy="11" r="10"/><path d="M19 48 Q19 24 36 24 Q54 24 54 48 Z"/>
      </svg>
      <span>Brokerage<br>Service</span>
    </div>
    <div class="service" style="left:372px; top:4px;">
      <svg width="56" height="48" viewBox="0 0 56 48">
        <path d="M8 6 H46 Q52 6 52 12 Q52 16 48 16 V42 H4 Q1 42 1 38 V34 H8 Z" fill="none" stroke="#e3242b" stroke-width="3.5"/>
        <line x1="14" y1="16" x2="30" y2="16" stroke="#e3242b" stroke-width="3"/>
        <line x1="14" y1="24" x2="26" y2="24" stroke="#e3242b" stroke-width="3"/>
        <path d="M26 32 L50 4 L55 8 L31 36 L24 38 Z" fill="#e3242b"/>
      </svg>
      <span>Policy Management<br>Systems</span>
    </div>
    <div class="service" style="left:704px; top:4px;">
      <svg width="46" height="50" viewBox="0 0 46 50">
        <path d="M3 2 H32 L40 10 V26 M26 47 H3 Z" fill="none" stroke="#e3242b" stroke-width="4"/>
        <path d="M3 2 V47 H24" fill="none" stroke="#e3242b" stroke-width="4"/>
        <line x1="10" y1="14" x2="28" y2="14" stroke="#e3242b" stroke-width="3"/>
        <line x1="10" y1="22" x2="24" y2="22" stroke="#e3242b" stroke-width="3"/>
        <line x1="10" y1="30" x2="20" y2="30" stroke="#e3242b" stroke-width="3"/>
        <circle cx="34" cy="33" r="8" fill="none" stroke="#e3242b" stroke-width="4"/>
        <path d="M28 40 L26 50 L34 46 L42 50 L40 40 Z" fill="#e3242b"/>
      </svg>
      <span>Claims TPA</span>
    </div>
    <div class="service" style="left:940px; top:2px;">
      <svg width="50" height="50" viewBox="0 0 50 50" fill="#e3242b">
        <rect x="1" y="0" width="3" height="50"/><rect x="1" y="47" width="48" height="3"/>
        <rect x="8" y="14" width="9" height="31"/><rect x="19" y="22" width="9" height="23"/><rect x="30" y="32" width="16" height="13"/>
      </svg>
      <span>Product<br>Analysis</span>
    </div>
  </section>

  <footer class="site-footer">
    <nav class="footer-nav">
      <a href="#">Home</a><span class="sep">|</span><a href="#">About us</a><span class="sep">|</span><a href="#">Services</a><span class="sep">|</span><a href="#">Contact us</a>
    </nav>
    <div class="copyright">Copyright &nbsp;©&nbsp; 2013 &nbsp; Brevanta RE Intermediaries. &nbsp; All rights reserved.</div>
    <a class="social one" href="#" aria-label="Social profile"></a>
    <a class="social two" href="#" aria-label="Social feed"></a>
  </footer>
</body>
</html>
```